Letterhead for financial advisor-insurance agent firm

Our company, Marlowe Thistle Insurance & Investments, is an insurance (health, life, home, auto, etc) and investment brokerage offering a suite of options to meet client needs. We need letterhead that is professional and embodies strength, security and sophistication.

Industry/Entity Type

Investment

```html
<!DOCTYPE html>
<html lang="en">
<head>
<meta charset="utf-8">
<title>Marlowe Thistle Insurance &amp; Investments — Letterhead</title>
<link href="https://fonts.googleapis.com/css2?family=Cinzel:wght@400;500&display=swap" rel="stylesheet">
<style>
  :root {
    --slate: #647a82;
    --navy: #2b3558;
    --paper: #ffffff;
  }
  html, body {
    margin: 0;
    padding: 0;
    overflow: hidden;
    background: var(--paper);
  }
  .letterhead {
    position: relative;
    width: 848px;
    height: 1200px;
    background: var(--paper);
    overflow: hidden;
  }
  .header-bands {
    position: absolute;
    top: 0;
    left: 0;
    width: 848px;
    height: 102px;
  }
  .band-slate { fill: var(--slate); }
  .band-navy { fill: var(--navy); }
  .brand {
    position: absolute;
    top: 12px;
    left: 0;
    width: 848px;
    text-align: center;
    font-family: "Cinzel", serif;
    color: var(--navy);
  }
  .brand-square {
    display: block;
    width: 52px;
    height: 52px;
    margin: 0 auto;
    box-sizing: border-box;
    border: 2px solid var(--navy);
  }
  .brand-name {
    margin: 6px 0 0;
    font-size: 22px;
    font-weight: 500;
    letter-spacing: 0.5px;
    line-height: 1;
  }
  .brand-tagline {
    margin: 3px 0 0;
    font-size: 8.5px;
    font-weight: 500;
    letter-spacing: 0.8px;
    line-height: 1;
  }
  .footer-bar {
    position: absolute;
    bottom: 0;
    left: 0;
    width: 848px;
    height: 18px;
    display: flex;
  }
  .footer-navy { width: 52px; background: var(--navy); }
  .footer-slate { flex: 1; background: var(--slate); }
</style>
</head>
<body>
  <div class="letterhead">
    <svg class="header-bands" viewBox="0 0 848 102" aria-hidden="true">
      <path class="band-slate" d="M0 0 H279 A206 206 0 0 0 222 102 H0 Z"/>
      <path class="band-navy" d="M848 0 V102 H624 A206 206 0 0 0 567 0 Z"/>
    </svg>

    <div class="brand">
      <span class="brand-square"></span>
      <p class="brand-name">Marlowe Thistle</p>
      <p class="brand-tagline">Insurance &amp; Investments</p>
    </div>

    <div class="footer-bar" aria-hidden="true">
      <div class="footer-navy"></div>
      <div class="footer-slate"></div>
    </div>
  </div>
</body>
</html>
```